New Web-Page Design Required

We need a new or initial web design for our page vorlan-grid.com. We provide products & services around infrastructure products. We have two products at the moment, but another 2 in the pipeline.
We want to have the following page structure (and part of the project is to design the 7 pages):
- Home
- Products
-One page per product
- Service
- Support
- About
- Contact (Email form)
The start page should include the following information:
- Twitter / Linkedin Links
- Telephone / Email or in general contact details
- News
- Maybe a link-box, where we can highlight/showcase things
- Link to our support portal, quite prominent
- Testimonials
It would be nice if the product pages would have a image header, where we can put up a screenshot or something. Links to datasheet and videos of the product would be nice as well.
We like the "big banner in the middle" designs, like these two Joomla examples. No need to copy them, it should just give you an idea.
http://www.pelmorthemes.com/itempreview/185
http://www.pelmorthemes.com/content/asj42/index.php
Budget for images available, so please use placeholders or ask us for specific photos/images, if you need them for your design.
Target Market(s)
Business-2-Business, Decision makers and Technical Leads
Industry/Entity Type
News
Look and feel

```html
<!DOCTYPE html>
<html lang="en">
<head>
<meta charset="utf-8">
<title>Vorlan Grid – Services</title>
<link rel="stylesheet" href="https://fonts.googleapis.com/css2?family=Roboto:wght@300;400;500;700&display=swap">
<style>
  :root {
    --topbar: #2d2d2d;
    --nav-blue: #2fb1dc;
    --teal: #12808d;
    --teal-bright: #14b5c4;
    --footer: #0d5f75;
    --footer-line: #0a4a5c;
    --page-bg: #dcdcdc;
    --panel: #ffffff;
    --text: #3a3a3a;
    --muted: #cfcfcf;
    --brand: #4a4a4a;
  }
  * { margin: 0; padding: 0; box-sizing: border-box; }
  html, body { width: 1200px; height: 1082px; overflow: hidden; }
  body { position: relative; font-family: "Roboto", sans-serif; background: #fff; color: var(--text); }
  .abs { position: absolute; }

  .topbar { left: 0; top: 0; width: 1200px; height: 36px; background: var(--topbar); }
  .social { top: 5px; width: 26px; height: 26px; border-radius: 3px; background: #4aa3d8; }
  .contact-line { top: 0; height: 36px; display: flex; align-items: center; color: #fff; font-size: 12px; }
  .contact-line svg { margin-right: 9px; }
  .contact-sep { margin: 0 14px; }

  .search { left: 671px; top: 6px; width: 335px; height: 34px; }

  .nav { left: 476px; top: 38px; width: 530px; height: 40px; }
  .nav-links { left: 476px; top: 38px; width: 530px; height: 40px; display: flex; align-items: center; justify-content: center; color: #fff; font-size: 14.5px; font-weight: 300; }
  .nav-links span.sep { margin: 0 13px; }
  .nav-links .active { text-decoration: underline; }

  .brand { left: 151px; top: 54px; height: 63px; display: flex; align-items: center; }
  .brand-dot { width: 60px; height: 60px; border-radius: 50%; background: var(--teal); margin-right: 14px; }
  .brand-name { font-size: 38px; font-weight: 500; color: var(--brand); letter-spacing: -0.5px; }

  .hero { left: 0; top: 122px; width: 1200px; height: 179px;
    background: linear-gradient(90deg, #1f8fc9 0%, #4ab7e6 25%, #8bd6f3 45%, #3aa9dc 70%, #1f8fc9 100%); }
  .hero-rule { left: 0; top: 301px; width: 1200px; height: 5px; background: linear-gradient(#b9b9b9, #e6e6e6); }

  .breadcrumb { left: 150px; top: 316px; font-size: 14px; font-weight: 300; color: var(--teal); }

  .content-bg { left: 0; top: 341px; width: 1200px; height: 660px; background: var(--page-bg); }

  .panel { background: var(--panel); border-radius: 6px; box-shadow: 0 0 6px rgba(0,0,0,.12); }
  .main-panel { left: 130px; top: 357px; width: 620px; height: 617px; }
  .main-head { left: 130px; top: 357px; width: 620px; height: 40px; border-radius: 6px 6px 0 0;
    background: linear-gradient(90deg, var(--teal) 0%, var(--teal-bright) 100%); display: flex; align-items: center; }
  .main-head svg { margin: 0 12px 0 13px; }
  .main-head h1 { font-size: 23px; font-weight: 500; color: #fff; }
  .main-photo { left: 130px; top: 397px; width: 620px; height: 207px;
    background: linear-gradient(90deg, #1c2a3c 0%, #3b4f6e 35%, #5a6a86 55%, #2d3a52 80%, #b8b7a4 100%); }
  .main-copy { left: 163px; top: 622px; width: 568px; font-size: 10.3px; font-weight: 300; line-height: 13px; }
  .main-copy p { margin-bottom: 12px; }
  .stages { left: 150px; top: 716px; border-left: 4px solid var(--teal-bright); padding-left: 12px; font-size: 10.3px; font-weight: 700; line-height: 13px; }

  .news-panel { left: 770px; top: 357px; width: 301px; height: 617px; }
  .news-head { left: 788px; top: 364px; font-size: 26px; font-weight: 400; color: var(--teal); }
  .news-rule { left: 772px; top: 403px; width: 297px; height: 2px; background: #d4d4d4; }
  .news-img-1 { left: 844px; top: 414px; width: 151px; height: 109px; border-radius: 6px;
    background: linear-gradient(135deg, #2b2b2b, #8a6c3e 50%, #2b2b2b); }
  .news-img-2 { left: 783px; top: 674px; width: 275px; height: 118px;
    background: linear-gradient(135deg, #0c2f52, #1e6aa3 50%, #0a2440); }
  .news-title { left: 784px; font-size: 18px; font-weight: 500; color: var(--teal); }
  .news-text { left: 786px; width: 274px; font-size: 10.6px; font-weight: 300; line-height: 13.2px; }
  .news-divider { left: 786px; top: 650px; width: 270px; height: 1px; background: #d8d8d8; }

  .footer { left: 0; top: 1001px; width: 1200px; height: 81px; background: var(--footer); border-top: 3px solid var(--footer-line); }
  .foot-text { color: #fff; font-size: 9.3px; }
  .foot-right { display: flex; align-items: center; }
</style>
</head>
<body>
  <div class="abs topbar"></div>
  <div class="abs social" style="left:135px"></div>
  <div class="abs social" style="left:171px"></div>

  <div class="abs contact-line" style="left:216px">
    <svg width="19" height="12" viewBox="0 0 19 12"><rect width="19" height="12" fill="#fff"/><path d="M0 0 L9.5 7 L19 0" stroke="#2d2d2d" fill="none" stroke-width="1.3"/></svg>
    info@vorlan-grid.com<span class="contact-sep">|</span>
    <svg width="13" height="13" viewBox="0 0 13 13"><path d="M2 0 L5 3 L3.5 5 Q5.5 8 8 9.5 L10 8 L13 11 L11 13 Q3 11 0 2 Z" fill="#fff"/></svg>
    0800 - 555 - 0199
  </div>

  <svg class="abs search" viewBox="0 0 335 34">
    <path d="M12 0 H265 L275 28 H0 Z" fill="#f1f1f1"/>
    <path d="M265 0 H318 L335 34 H275 Z" fill="#bfe6f2"/>
    <circle cx="302" cy="13" r="6" fill="none" stroke="#2d2d2d" stroke-width="1.6"/>
    <line x1="298" y1="17" x2="292" y2="23" stroke="#2d2d2d" stroke-width="2"/>
  </svg>

  <svg class="abs nav" viewBox="0 0 530 40"><path d="M0 0 H530 L512 40 H18 Z" fill="var(--nav-blue)"/></svg>
  <nav class="abs nav-links">
    <span>Home</span><span class="sep">|</span><span>About Us</span><span class="sep">|</span><span>Products</span><span class="sep">|</span><span>Services</span><span class="sep">|</span><span class="active">Support</span><span class="sep">|</span><span>Contact</span>
  </nav>

  <div class="abs brand"><div class="brand-dot"></div><span class="brand-name">Vorlan Grid</span></div>

  <div class="abs hero" role="img" aria-label="Blue-tinted photograph of server racks in a data center aisle"></div>
  <div class="abs hero-rule"></div>

  <div class="abs breadcrumb">home &gt; services</div>

  <div class="abs content-bg"></div>

  <div class="abs panel main-panel"></div>
  <div class="abs main-head">
    <svg width="26" height="28" viewBox="0 0 26 28"><rect x="0" y="2" width="11" height="26" rx="2" fill="#fff" opacity=".85"/><rect x="13" y="0" width="13" height="28" rx="2" fill="#fff" opacity=".85"/><rect x="16" y="5" width="7" height="3" fill="var(--teal)"/><rect x="16" y="11" width="7" height="3" fill="var(--teal)"/></svg>
    <h1>Services</h1>
  </div>
  <div class="abs main-photo" role="img" aria-label="Close-up photograph of server hardware with glowing status lights"></div>
  <div class="abs main-copy">
    <p>Installation &amp; Professional Services can be provided by us or competent partners. In any case, you will get very experienced software consultants, who can fix every issue.</p>
    <p>Our service offerings include everything from infrastructure consulting, installation of the software and training how to use it and to get the best out of it. We can help you at any stage of your project or we can even do the full implementation for you. Usually our projects will follow the following process and stages:</p>
  </div>
  <ul class="abs stages" style="list-style:none">
    <li>• Infrastructure Design (Cluster vs. Non Cluster, Security, Uptime considerations)</li>
    <li>• Installation (n.Insights, VCD/C, Database, LDAP Connectivity)</li>
    <li>• Configuration (Performance Reviews, Push-Notification Configuration)</li>
    <li>• Post-Installation Testing</li>
    <li>• Training</li>
  </ul>

  <div class="abs panel news-panel"></div>
  <h2 class="abs news-head">News</h2>
  <div class="abs news-rule"></div>
  <div class="abs news-img-1" role="img" aria-label="Tablet and smartphones showing a mobile app"></div>
  <h3 class="abs news-title" style="top:535px">News Title 1</h3>
  <p class="abs news-text" style="top:566px">Lorem ipsum dolor sit amet, consectetuer adipiscing elit, sed diam nonummy nibh euismod tincidunt ut laoreet dolore magna aliquam erat volutpat. Ut wisi enim ad minim veniam, quis nostrud exerci tation ullamcorper suscipit lobortis nisl ut aliquip ex ea commodo conse-</p>
  <div class="abs news-divider"></div>
  <div class="abs news-img-2" role="img" aria-label="Blue screen of source code"></div>
  <h3 class="abs news-title" style="top:820px">News Title 2</h3>
  <p class="abs news-text" style="top:852px">Lorem ipsum dolor sit amet, consectetuer adipiscing elit, sed diam nonummy nibh euismod tincidunt ut laoreet dolore magna aliquam erat volutpat. Ut wisi enim ad minim veniam, quis nostrud exerci tation ullamcorper suscipit lobortis nisl ut aliquip ex ea commodo consequat. Duis autem vel eum iriure dolor in hendrerit in vulputate velit esse molestie consequat, vel illum dolore</p>

  <footer class="abs footer"></footer>
  <div class="abs foot-text" style="left:145px;top:1020px">Home &nbsp;&nbsp;| &nbsp;&nbsp;Products &nbsp;&nbsp;| &nbsp;&nbsp;Services &nbsp;| &nbsp;&nbsp;Support &nbsp;&nbsp;| &nbsp;&nbsp;Contact</div>
  <div class="abs foot-text" style="left:145px;top:1042px;line-height:12px">Copyright © 2013 Vorlan Grid. All rights reserved.<br>Korvex, Tallyscope are either registered trademarks or trademarks of Korvex Corporation in the United States and/or other countries.</div>
  <div class="abs foot-text" style="left:925px;top:1020px">Terms and Condition | Privacy</div>
  <div class="abs foot-text foot-right" style="left:818px;top:1039px">
    <svg width="19" height="12" viewBox="0 0 19 12" style="margin-right:10px"><rect width="19" height="12" fill="#fff"/><path d="M0 0 L9.5 7 L19 0" stroke="#0d5f75" fill="none" stroke-width="1.3"/></svg>
    info@vorlan-grid.com<span style="margin:0 12px">|</span>
    <svg width="11" height="11" viewBox="0 0 13 13" style="margin-right:7px"><path d="M2 0 L5 3 L3.5 5 Q5.5 8 8 9.5 L10 8 L13 11 L11 13 Q3 11 0 2 Z" fill="#fff"/></svg>
    0800 - 555 - 0199
  </div>
</body>
</html>
```